I need a business Card Design for my practice , i am clinical herbalist. I am a herbalist specializing in Lyme disease, autism, autoimmune diseases, difficult to cure diseasesDifficult to cure diseases. In my innovative practice i link traditional medicine, herbs with science, immunologu ,pharmacology.

Industry/Entity Type

Business

Contact Information for Business Card

My company name : OŚRODEK ZIELNIK
My name : Piotr Kaleta
Name of my profession : Fitoterapeuta
In Polish language Fitoterapeuta is Herbalist .

e-mail: piotrkaleta@osrodekzielnik.com
www.osrodek-zielnik.pl
phone : 604 587 231
My company adress : Dąbrowa Sitnicka 41 , 38-415 Brzozówka
I dont have logo .

Requirements
Nice to have
• My company

```html
<!DOCTYPE html>
<html lang="pl">
<head>
<meta charset="UTF-8">
<title>Ośrodek Zielnik – wizytówka</title>
<link rel="stylesheet" href="https://fonts.googleapis.com/css2?family=Michroma&family=Open+Sans:wght@400;600&display=swap">
<style>
  :root {
    --orange: #f28a30;
    --charcoal: #333233;
    --light-grey: #e6e7e8;
    --white: #ffffff;
    --text: #3a3a3a;
    --backdrop: #efefef;
  }
  * { box-sizing: border-box; margin: 0; padding: 0; }
  html, body {
    width: 1200px;
    height: 1200px;
    overflow: hidden;
    background: var(--backdrop);
  }
  .canvas {
    width: 1200px;
    height: 1200px;
    display: flex;
    align-items: center;
    justify-content: center;
  }
  .business-card {
    width: 1000px;
    height: 580px;
    background: var(--white);
    display: grid;
    grid-template-rows: 165px 130px 1fr 1fr;
    grid-template-columns: 1fr 1fr;
    box-shadow: 0 8px 24px rgba(0,0,0,0.12);
    font-family: "Open Sans", sans-serif;
    color: var(--text);
  }
  .brand-band {
    grid-column: 1 / 3;
    background: var(--orange);
    display: flex;
    align-items: center;
    justify-content: center;
  }
  .brand-name {
    font-family: "Michroma", sans-serif;
    color: var(--white);
    font-size: 44px;
    letter-spacing: 6px;
    font-weight: 400;
    white-space: nowrap;
  }
  .person-band {
    grid-column: 1 / 3;
    background: var(--charcoal);
    color: var(--white);
    display: flex;
    flex-direction: column;
    align-items: center;
    justify-content: center;
  }
  .person-name {
    font-size: 38px;
    font-weight: 400;
    line-height: 1.15;
  }
  .person-title {
    font-size: 19px;
    margin-top: 2px;
  }
  .contact-cell {
    display: flex;
    flex-direction: column;
    align-items: center;
    justify-content: center;
    gap: 12px;
    font-size: 21px;
    white-space: nowrap;
  }
  .contact-cell.shaded { background: var(--light-grey); }
  .contact-icon { width: 30px; height: 30px; fill: var(--orange); }
</style>
</head>
<body>
<main class="canvas">
  <article class="business-card">
    <header class="brand-band">
      <h1 class="brand-name">OŚRODEK ZIELNIK</h1>
    </header>
    <section class="person-band">
      <h2 class="person-name">Piotr Kaleta</h2>
      <p class="person-title">Fitoterapeuta</p>
    </section>

    <div class="contact-cell shaded phone">
      <svg class="contact-icon" viewBox="0 0 24 24" aria-hidden="true">
        <path d="M6.6 10.8a15.1 15.1 0 0 0 6.6 6.6l2.2-2.2c.3-.3.7-.4 1-.2 1.1.4 2.3.6 3.6.6.6 0 1 .4 1 1V20c0 .6-.4 1-1 1C10.6 21 3 13.4 3 4c0-.6.4-1 1-1h3.5c.6 0 1 .4 1 1 0 1.3.2 2.5.6 3.6.1.3 0 .7-.2 1L6.6 10.8z"/>
      </svg>
      <span>604 587 231</span>
    </div>

    <div class="contact-cell email">
      <svg class="contact-icon" viewBox="0 0 24 24" aria-hidden="true">
        <path d="M2 5h20v14H2z"/>
        <path d="M2.5 5.5l9.5 7.5 9.5-7.5" fill="none" stroke="#fff" stroke-width="1.4"/>
        <path d="M2.5 18.5l7-6 M21.5 18.5l-7-6" fill="none" stroke="#fff" stroke-width="1.2"/>
      </svg>
      <span>piotrkaleta@osrodekzielnik.com</span>
    </div>

    <div class="contact-cell website">
      <svg class="contact-icon" viewBox="0 0 24 24" aria-hidden="true">
        <circle cx="12" cy="12" r="10"/>
        <g fill="none" stroke="#fff" stroke-width="1.2">
          <ellipse cx="12" cy="12" rx="4.5" ry="10"/>
          <path d="M12 2v20 M2 12h20 M4 7h16 M4 17h16"/>
        </g>
      </svg>
      <span>www.osrodek-zielnik.pl</span>
    </div>

    <div class="contact-cell shaded address">
      <svg class="contact-icon" viewBox="0 0 24 24" aria-hidden="true">
        <path d="M12 2a7 7 0 0 0-7 7c0 5.2 7 13 7 13s7-7.8 7-13a7 7 0 0 0-7-7zm0 9.5a2.5 2.5 0 1 1 0-5 2.5 2.5 0 0 1 0 5z"/>
      </svg>
      <span>Dąbrowa Sitnicka 41 , 38-415 Brzozówka</span>
    </div>
  </article>
</main>
</body>
</html>
```